Business Card Design

I need a business card design for a photography business that specializes in headshots and portraits.

Target Market(s)

Business professionals, actors, actresses

Industry/Entity Type

Business

Contact Information for Business Card

Corvin Lane Photography, Greg Wilmot, 1187 Kestrel Avenue, Suite 416, Fort Wayne, IN 46815, 260.555.0148, www.corvinlanephoto.example. greg.wilmot@corvinlanephoto.example

Requirements
Must have
• The business card should state the type of photography services offered: headshots and portraits.

```html
<!DOCTYPE html>
<html lang="en">
<head>
<meta charset="utf-8">
<title>Corvin Lane Photography — Business Card</title>
<link href="https://fonts.googleapis.com/css2?family=Cormorant+Garamond:ital,wght@1,500&family=Open+Sans:ital,wght@0,400;1,400&display=swap" rel="stylesheet">
<style>
  :root {
    --stage: #1e1e20;
    --card: #9c9c9c;
    --card-edge: #b4b4b4;
    --ink: #ffffff;
    --ink-soft: #f2f2f2;
  }
  * { box-sizing: border-box; margin: 0; padding: 0; }
  html, body {
    width: 1200px;
    height: 1000px;
    overflow: hidden;
    background: var(--stage);
  }
  .stage {
    width: 1200px;
    height: 1000px;
    display: flex;
    align-items: center;
    justify-content: center;
  }
  .business-card {
    position: relative;
    width: 980px;
    height: 560px;
    background: var(--card);
    border: 1px solid var(--card-edge);
    border-radius: 10px;
    color: var(--ink);
    font-family: "Open Sans", Arial, sans-serif;
  }
  .studio-name {
    position: absolute;
    top: 56px;
    left: 480px;
    right: 40px;
    text-align: center;
    font-family: "Cormorant Garamond", Georgia, serif;
    font-style: italic;
    font-weight: 500;
    font-size: 46px;
    line-height: 56px;
    letter-spacing: 0.5px;
  }
  .services {
    position: absolute;
    top: 118px;
    left: 480px;
    right: 40px;
    text-align: center;
    font-size: 18px;
    letter-spacing: 2px;
    text-transform: uppercase;
    color: var(--ink-soft);
  }
  .person-name {
    position: absolute;
    top: 226px;
    left: 480px;
    right: 40px;
    text-align: center;
    font-size: 40px;
    line-height: 54px;
    font-weight: 400;
  }
  .contact-list {
    position: absolute;
    top: 226px;
    left: 40px;
    width: 420px;
    list-style: none;
    font-size: 18px;
    line-height: 28px;
    color: var(--ink-soft);
  }
  .contact-item {
    display: flex;
    align-items: center;
    gap: 8px;
    white-space: nowrap;
  }
  .contact-item--continued { padding-left: 26px; }
  .contact-icon { width: 18px; height: 18px; flex: none; }
  .website {
    position: absolute;
    right: 44px;
    bottom: 40px;
    font-style: italic;
    font-size: 20px;
    color: var(--ink-soft);
  }
</style>
</head>
<body>
<main class="stage">
  <article class="business-card">
    <h1 class="studio-name">Corvin Lane Photography</h1>
    <p class="services">Headshots &amp; Portraits</p>
    <p class="person-name">Greg Wilmot</p>
    <ul class="contact-list">
      <li class="contact-item">
        <svg class="contact-icon" viewBox="0 0 20 20" aria-hidden="true">
          <circle cx="10" cy="10" r="9" fill="none" stroke="#fff" stroke-width="1.6"/>
          <path d="M7 5.5c-.8.5-1.2 1.4-.9 2.4.7 2.4 2.6 4.5 5 5.5 1 .4 1.9 0 2.4-.8l-1.6-1.6-1.2.6c-1-.5-1.9-1.4-2.4-2.4l.6-1.2z" fill="#fff"/>
        </svg>
        <span>260.555.0148</span>
      </li>
      <li class="contact-item">
        <svg class="contact-icon" viewBox="0 0 20 20" aria-hidden="true">
          <circle cx="10" cy="10" r="9" fill="none" stroke="#fff" stroke-width="1.6"/>
          <path d="M5.5 6.5h9v7h-9z" fill="none" stroke="#fff" stroke-width="1.3"/>
          <path d="M5.5 6.5l4.5 4 4.5-4" fill="none" stroke="#fff" stroke-width="1.3"/>
        </svg>
        <span>greg.wilmot@corvinlanephoto.example</span>
      </li>
      <li class="contact-item">
        <svg class="contact-icon" viewBox="0 0 20 20" aria-hidden="true">
          <circle cx="10" cy="10" r="9" fill="none" stroke="#fff" stroke-width="1.6"/>
          <path d="M10 4.5a3.5 3.5 0 0 0-3.5 3.5c0 2.6 3.5 7 3.5 7s3.5-4.4 3.5-7A3.5 3.5 0 0 0 10 4.5zm0 4.9a1.4 1.4 0 1 1 0-2.8 1.4 1.4 0 0 1 0 2.8z" fill="#fff"/>
        </svg>
        <span>1187 Kestrel Avenue, Suite 416</span>
      </li>
      <li class="contact-item contact-item--continued">Fort Wayne, IN 46815</li>
    </ul>
    <p class="website">www.corvinlanephoto.example</p>
  </article>
</main>
</body>
</html>
```